Flyer Design

The company nane is "MARLO DUNE EARTHWORKS" it is a earthmoving company using a skid steer or korvex with tracks, the type of work I will be doing range from site cleans, pavings preps, house pads, final trim, landscaping, pool digs. Call 0491570156

i have posted a foto of the new design for the logo, please incorporate somehow, also i am using a velmor glide rig vk30 skid steer, i am not using a front end loader or digger or anu other earthmoving gear so dont use them.

Reason: more time for more ideas

include easy narrow access

Very experienced in all aspects of korvex work. Rubbish removal. House and shed pads. Paving prep Concrete removal. Lawn removal. Clearing Limestone driveways. Limestone block lifting. Levelling.

If you want it done fast. Wether your after site cleans, paving preps, earth moving, house pads, final trim or yard demos we cater for the lot. Our specialty equipment can do the lot

I have uploaded 2 new pictures, one is the actual logo of the business and the other is the picture I want used on the flyer, think outside the box

House

```html
<!DOCTYPE html>
<html lang="en">
<head>
<meta charset="utf-8">
<title>Marlo Dune Earthworks – Flyer</title>
<link rel="stylesheet" href="https://fonts.googleapis.com/css2?family=Oswald:wght@600;700&family=Saira+Condensed:wght@500;600&family=Russo+One&display=swap">
<style>
  :root {
    --paper: #e2e2df;
    --paper-dark: #cfd0cc;
    --ink-logo: #3b3f45;
    --navy: #1d2231;
    --box-brown: #7b5b3d;
    --box-brown-dark: #684a30;
    --band-rust: #a0401b;
    --band-rust-dark: #7e2e12;
    --cream: #f1e6d2;
    --white: #ffffff;
  }
  * { margin: 0; padding: 0; box-sizing: border-box; }
  html, body { width: 1200px; height: 850px; overflow: hidden; background: var(--paper); }
  .flyer {
    position: relative;
    width: 1200px;
    height: 850px;
    overflow: hidden;
    background: linear-gradient(180deg, var(--paper) 0%, var(--paper-dark) 100%);
  }
  .layer { position: absolute; inset: 0; width: 1200px; height: 850px; }

  .brand {
    position: absolute;
    left: 440px;
    top: 122px;
    width: 480px;
    text-align: center;
    font-family: "Oswald", "Arial Narrow", sans-serif;
    font-weight: 700;
    color: var(--ink-logo);
    text-transform: uppercase;
    line-height: 1;
  }
  .brand__name { display: block; font-size: 74px; letter-spacing: 1px; }
  .brand__sub { display: block; font-size: 44px; letter-spacing: 8px; margin-top: 4px; }

  .tagline {
    position: absolute;
    left: 482px;
    top: 262px;
    width: 578px;
    height: 44px;
    border-radius: 22px;
    background: var(--navy);
    color: var(--white);
    font-family: "Saira Condensed", "Arial Narrow", sans-serif;
    font-weight: 500;
    font-size: 38px;
    line-height: 44px;
    text-align: center;
    letter-spacing: 0.3px;
  }

  .services {
    position: absolute;
    left: 640px;
    top: 322px;
    width: 402px;
    height: 372px;
    border-radius: 18px;
    background: linear-gradient(180deg, var(--box-brown) 0%, var(--box-brown-dark) 100%);
    box-shadow: 0 4px 14px rgba(0,0,0,0.35);
    padding: 22px 0 0 24px;
    list-style: none;
  }
  .services__item {
    position: relative;
    padding-left: 44px;
    font-family: "Oswald", "Arial Narrow", sans-serif;
    font-weight: 600;
    font-size: 45px;
    line-height: 52px;
    color: var(--white);
    text-transform: uppercase;
    letter-spacing: 0.5px;
  }
  .services__item::before {
    content: "";
    position: absolute;
    left: 6px;
    top: 22px;
    width: 9px;
    height: 9px;
    border-radius: 50%;
    background: var(--white);
  }

  .contact__label {
    position: absolute;
    left: 386px;
    top: 696px;
    font-family: "Saira Condensed", "Arial Narrow", sans-serif;
    font-weight: 600;
    font-size: 46px;
    line-height: 56px;
    color: var(--cream);
    letter-spacing: 0.3px;
  }
  .contact__phone {
    position: absolute;
    left: 372px;
    top: 746px;
    font-family: "Russo One", "Arial Black", sans-serif;
    font-size: 80px;
    line-height: 84px;
    color: var(--white);
    letter-spacing: 10px;
    text-shadow: 0 3px 6px rgba(0,0,0,0.35);
    white-space: nowrap;
  }
  .contact__rule { position: absolute; background: rgba(255,255,255,0.7); }
  .contact__rule--left { left: 355px; top: 738px; width: 1px; height: 82px; }
  .contact__rule--right { left: 1056px; top: 724px; width: 1px; height: 96px; }
  .contact__rule--base { left: 355px; top: 820px; width: 120px; height: 1px; }
</style>
</head>
<body>
<main class="flyer">

  <svg class="layer site-photo" viewBox="0 0 1200 850" role="img" aria-label="Photo of a cleared bush site with bare trees on the left and a close-up of loose brown earth on the right">
    <defs>
      <linearGradient id="siteTones" x1="0" y1="0" x2="1" y2="0.3">
        <stop offset="0" stop-color="#a19d92"/>
        <stop offset="0.3" stop-color="#7a7465"/>
        <stop offset="0.55" stop-color="#6e5a44"/>
        <stop offset="0.75" stop-color="#6e5138"/>
        <stop offset="1" stop-color="#5a3d26"/>
      </linearGradient>
      <linearGradient id="groundTones" x1="0" y1="0" x2="0" y2="1">
        <stop offset="0.55" stop-color="#8a6a48" stop-opacity="0"/>
        <stop offset="1" stop-color="#8a6a48" stop-opacity="0.8"/>
      </linearGradient>
    </defs>
    <path d="M0,235 C180,195 420,215 620,245 C780,268 900,200 1000,150 C1080,115 1150,118 1200,120 L1200,850 L0,850 Z" fill="url(#siteTones)"/>
    <path d="M0,235 C180,195 420,215 620,245 C780,268 900,200 1000,150 C1080,115 1150,118 1200,120 L1200,850 L0,850 Z" fill="url(#groundTones)"/>
  </svg>

  <svg class="layer machine-photos" viewBox="0 0 1200 850">
    <defs>
      <linearGradient id="machineTones" x1="0" y1="0" x2="0" y2="1">
        <stop offset="0" stop-color="#d9d9d5"/>
        <stop offset="0.35" stop-color="#3a3d42"/>
        <stop offset="1" stop-color="#18191c"/>
      </linearGradient>
      <linearGradient id="spillTones" x1="0" y1="0" x2="0" y2="1">
        <stop offset="0" stop-color="#2a2a2c"/>
        <stop offset="0.35" stop-color="#6b4a2e"/>
        <stop offset="1" stop-color="#8a6440"/>
      </linearGradient>
    </defs>
    <g role="img" aria-label="Cut-out photo of a tracked compact loader with its bucket raised, shown small behind the company name">
      <rect x="255" y="62" width="215" height="236" rx="22" fill="url(#machineTones)"/>
    </g>
    <g role="img" aria-label="Photo of a tracked compact loader tipping a bucket of soil in the foreground">
      <rect x="8" y="292" width="480" height="448" rx="28" fill="url(#machineTones)"/>
      <rect x="372" y="326" width="250" height="300" rx="26" fill="url(#spillTones)"/>
    </g>
  </svg>

  <svg class="layer contact-band" viewBox="0 0 1200 850" aria-hidden="true">
    <defs>
      <linearGradient id="rust" x1="0" y1="0" x2="1" y2="0">
        <stop offset="0" stop-color="#7e2e12"/>
        <stop offset="0.5" stop-color="#a0401b"/>
        <stop offset="1" stop-color="#7e2e12"/>
      </linearGradient>
    </defs>
    <path d="M0,780 C180,720 360,690 560,680 C780,670 980,655 1200,630 L1200,850 L0,850 Z" fill="url(#rust)"/>
    <path d="M420,688 C640,660 900,650 1200,615" fill="none" stroke="#b5512a" stroke-width="6"/>
    <path d="M480,676 C700,650 940,640 1200,605" fill="none" stroke="#8c3415" stroke-width="3" opacity="0.8"/>
  </svg>

  <h1 class="brand">
    <span class="brand__name">Marlo Dune</span>
    <span class="brand__sub">Earthworks</span>
  </h1>

  <p class="tagline">Earthmoving Company Specialises in</p>

  <ul class="services">
    <li class="services__item">Site Cleaning</li>
    <li class="services__item">Pavings Preps</li>
    <li class="services__item">House Pads</li>
    <li class="services__item">Final Trimming</li>
    <li class="services__item">Landscaping</li>
    <li class="services__item">Pool Digging</li>
  </ul>

  <section class="contact">
    <span class="contact__rule contact__rule--left"></span>
    <span class="contact__rule contact__rule--right"></span>
    <span class="contact__rule contact__rule--base"></span>
    <p class="contact__label">For More Info Contact:</p>
    <p class="contact__phone">0491 570 156</p>
  </section>

</main>
</body>
</html>
```